lantern quill flyer

lantern quill, analysing tapes in reverse and hypnotherapy services - logo and design similar to website - http://www.lanternquill.com - flyer should be half A4 size - workshop on one side, training class on the other

Industry/Entity Type

Hypnotherapy

Colors
0455a3
3176b5

```html
<!DOCTYPE html>
<html lang="en">
<head>
<meta charset="utf-8">
<title>Lantern Quill Intensive Workshop</title>
<link href="https://fonts.googleapis.com/css2?family=Raleway:wght@400;500;600;700&family=Josefin+Sans:ital,wght@0,300;1,300&display=swap" rel="stylesheet">
<style>
  :root {
    --brand-blue: #0455a3;
    --brand-blue-light: #3176b5;
    --badge-light: #2ea3dc;
    --ink: #111111;
    --body-grey: #555555;
    --frame-grey: #b9c3d6;
    --paper: #ffffff;
  }
  * { margin: 0; padding: 0; box-sizing: border-box; }
  html, body { width: 846px; height: 1200px; overflow: hidden; background: var(--paper); }
  .flyer {
    position: relative;
    width: 846px;
    height: 1200px;
    overflow: hidden;
    font-family: "Raleway", sans-serif;
    background: var(--paper);
  }
  .hero-photo {
    position: absolute;
    left: 0; top: 0;
    width: 846px; height: 742px;
    background: linear-gradient(100deg, #eeeeee 0%, #d9d9d9 40%, #bfbfbf 60%, #e4e4e4 80%, #f3f3f3 100%);
  }
  .top-band {
    position: absolute;
    left: 0; top: 0;
    width: 846px; height: 171px;
    background: var(--brand-blue);
  }
  .title {
    position: absolute;
    right: 60px;
    top: 100px;
    text-align: right;
    font-weight: 500;
    line-height: 1;
  }
  .title-brand { display: block; color: var(--paper); font-size: 62px; height: 72px; }
  .title-event { display: block; color: var(--brand-blue); font-size: 62px; }
  .topics {
    position: absolute;
    left: 57px;
    top: 505px;
    list-style: none;
  }
  .topics li {
    display: table;
    background: var(--brand-blue);
    color: var(--paper);
    font-weight: 600;
    font-size: 19px;
    padding: 6px 6px 6px 6px;
    margin-bottom: 12px;
    height: 35px;
    letter-spacing: 0.2px;
  }
  .intro {
    position: absolute;
    left: 58px;
    top: 770px;
    width: 420px;
    font-size: 16px;
    line-height: 1.2;
    color: var(--body-grey);
  }
  .testimonial {
    position: absolute;
    left: 57px;
    width: 402px;
    border: 1px solid var(--frame-grey);
    padding: 9px 12px 8px 11px;
    font-family: "Josefin Sans", sans-serif;
    font-weight: 300;
    font-size: 11.5px;
    line-height: 1.4;
    color: #333333;
  }
  .testimonial-first { top: 853px; height: 116px; }
  .testimonial-second { top: 983px; height: 78px; }
  .testimonial cite {
    display: block;
    text-align: right;
    font-style: italic;
    margin-top: 2px;
  }
  .event-badge {
    position: absolute;
    left: 490px;
    top: 738px;
    width: 310px;
    height: 270px;
  }
  .event-badge svg { position: absolute; left: 0; top: 0; }
  .badge-text {
    position: absolute;
    left: 0; top: 22px;
    width: 300px;
    text-align: center;
    color: var(--paper);
    font-weight: 700;
    font-size: 21px;
    line-height: 1.2;
  }
  .badge-rule {
    width: 214px;
    height: 1px;
    margin: 12px auto 10px;
    background: rgba(255,255,255,0.7);
  }
  .badge-price { font-size: 27px; }
  .cta-bar {
    position: absolute;
    left: 57px;
    top: 1092px;
    background: var(--brand-blue);
    color: var(--paper);
    font-weight: 700;
    font-size: 20px;
    padding: 3px 5px;
    height: 30px;
  }
  .contact {
    position: absolute;
    left: 58px;
    top: 1128px;
    font-weight: 700;
    font-size: 16px;
    color: var(--ink);
  }
</style>
</head>
<body>
<main class="flyer">
  <div class="hero-photo" role="img" aria-label="Black and white photograph of a smiling man and woman in soft focus"></div>
  <div class="top-band"></div>
  <h1 class="title">
    <span class="title-brand">Lantern Quill</span>
    <span class="title-event">Intensive Workshop</span>
  </h1>

  <ul class="topics">
    <li>The History of Lantern Quill</li>
    <li>The Basics of Lantern Quill Theory</li>
    <li>Basic Analysis Techniques &amp; Procedures</li>
    <li>How to Use The Lantern Quill Professional Software</li>
    <li>A Chance to Hear Your Own Speech Reversals</li>
  </ul>

  <p class="intro">This workshop will prove to be a fascinating and explorative journey into the sub-conscious, the unconscious, the collective consciousness, and the Spirit.</p>

  <blockquote class="testimonial testimonial-first">
    “I had a very bizarre pattern in my life that continually sabotaged my efforts to improve. Whenever I told anyone about it, they thought I was making it up. With Lantern Quill I was able to see exactly what was going on and why it was going on. In four months time I completely transformed a situation I had been working on for 20 years.”
    <cite>- Dan Morrow, Golf Pro, San Diego, CA</cite>
  </blockquote>
  <blockquote class="testimonial testimonial-second">
    “Lantern Quill has given me more freedom in my life. Obstacles that limited me are not there anymore. I am studying for a new career that I would only have dreamed about before.”
    <cite>- Clara Denholm, Engineer Computer Draftsperson</cite>
  </blockquote>

  <div class="event-badge">
    <svg width="310" height="270" viewBox="0 0 310 270" aria-hidden="true">
      <defs>
        <linearGradient id="badgeFill" x1="0" y1="0" x2="1" y2="0.4">
          <stop offset="0" stop-color="var(--badge-light)"/>
          <stop offset="1" stop-color="var(--brand-blue)"/>
        </linearGradient>
      </defs>
      <g fill="#d8d8d8" transform="translate(0 30)">
        <rect x="30" y="25" width="240" height="180"/>
        <circle cx="50" cy="25" r="25"/><circle cx="100" cy="20" r="25"/><circle cx="150" cy="18" r="25"/><circle cx="200" cy="20" r="25"/><circle cx="250" cy="25" r="25"/>
        <circle cx="50" cy="205" r="25"/><circle cx="100" cy="210" r="25"/><circle cx="150" cy="212" r="25"/><circle cx="200" cy="210" r="25"/><circle cx="250" cy="205" r="25"/>
        <circle cx="25" cy="70" r="25"/><circle cx="22" cy="115" r="25"/><circle cx="25" cy="160" r="25"/>
        <circle cx="275" cy="70" r="25"/><circle cx="278" cy="115" r="25"/><circle cx="275" cy="160" r="25"/>
      </g>
      <g fill="url(#badgeFill)">
        <rect x="30" y="25" width="240" height="180"/>
        <circle cx="50" cy="25" r="25"/><circle cx="100" cy="20" r="25"/><circle cx="150" cy="18" r="25"/><circle cx="200" cy="20" r="25"/><circle cx="250" cy="25" r="25"/>
        <circle cx="50" cy="205" r="25"/><circle cx="100" cy="210" r="25"/><circle cx="150" cy="212" r="25"/><circle cx="200" cy="210" r="25"/><circle cx="250" cy="205" r="25"/>
        <circle cx="25" cy="70" r="25"/><circle cx="22" cy="115" r="25"/><circle cx="25" cy="160" r="25"/>
        <circle cx="275" cy="70" r="25"/><circle cx="278" cy="115" r="25"/><circle cx="275" cy="160" r="25"/>
      </g>
    </svg>
    <div class="badge-text">
      <p>Coming to London<br>May 17th &amp; 18th 2014</p>
      <div class="badge-rule"></div>
      <p>Special price of<br><span class="badge-price">$497.00</span><br>when you register<br>today</p>
    </div>
  </div>

  <p class="cta-bar">Seats are filling fast. Reserve your place today!</p>
  <p class="contact">Call London 0203 5550172 or register online at www.lanternquill.com</p>
</main>
</body>
</html>
```